Website design for online service business

The company provides the following services:
1 - consultancy services on existing products (like tallydesk and brisk 354)
2 - Coaching services - Coach someone on services like using/developing features with existing products, or teach how to be more productive, or improve their business using automation, etc
3 - Training
- Online training on demand on existing products via vokra (like in Tallydesk and brisk 365)
- Online courses through videos lessons and scripts by offering information products where people will need to register and pay in advance to access the online course. (productivity courses for example)

- The goal is for clients to book time with me for one of those areas without too many clicks.
- Clients will be able to Book time using an integration (it would be good to have the layout integrated with the site.) with this https://planner.brisk-suite.example/owa/calendar/BrightKelpStudio1@brightkelpstudio.bookhub.example/bookings/

- there will be areas for which i whish to build a VIP mailing list. It's referenced on the wireframes

References:
https://www.lanternfieldnotes.example/about/about-dorvan/
https://www.pebblecompass.example/
https://tallydeskguide.example/

Target Market(s)

- Small businesses
- Freelancers

Industry/Entity Type

Business

Number of Pages Required

5+ page

Font styles to use
Sans Serif

Colors

Designer to choose colors to be used in the design.

Requirements
Must have
• Must have the design optimized to the less clicks possible to achieve any action
• The colors of the site should follow the logo (provided in attach)
• It should use other color that belong to the same pallet of colors
• Should contain colors that incentivizes people to click and book something
• Images and backgrounds should be made available
• All images sizes and colors should be provided to be able to develop the site according to the design
Nice to have
• The bookings for the time should be integrated within the design. If not possible a redirection to it can work as well.
Should not have
• Links to social media
• Pop-ups
• Intrusive navigations (like navigation bares on the left or right hand side)
• Should not be a template used by many people

```html
<!DOCTYPE html>
<html lang="en">
<head>
<meta charset="utf-8">
<title>Bright Kelp – Home</title>
<link rel="stylesheet" href="https://fonts.googleapis.com/css2?family=Indie+Flower&family=Mulish:wght@400;600;700;800&display=swap">
<style>
  :root {
    --brand-blue: #0b6ea5;
    --brand-blue-text: #1b7db8;
    --sky: #a6e0fa;
    --sky-deco: #97d6f3;
    --orange: #f7941d;
    --ink: #3a3a3a;
    --ink-soft: #4b4b4b;
    --white: #ffffff;
    --hero-top: #8e8f8c;
    --hero-bottom: #5f5a55;
    --photo-a: #6f7a6a;
    --photo-b: #a69a8e;
    --icon-fill: #6cc3e8;
  }
  * { box-sizing: border-box; margin: 0; padding: 0; }
  html, body { width: 800px; height: 1200px; overflow: hidden; }
  body { position: relative; background: var(--white); font-family: "Mulish", Arial, sans-serif; color: var(--ink); }

  /* header */
  .site-header { position: absolute; left: 0; top: 0; width: 800px; height: 60px; background: var(--white); }
  .brand { position: absolute; left: 100px; top: 18px; display: flex; align-items: center; gap: 6px; }
  .brand-mark { width: 12px; height: 12px; background: var(--brand-blue); }
  .brand-name { font-weight: 800; font-size: 15px; letter-spacing: 1px; color: var(--brand-blue); }
  .main-nav { position: absolute; left: 278px; top: 44px; display: flex; font-size: 9.5px; letter-spacing: .4px; }
  .main-nav a { text-decoration: none; color: var(--ink-soft); margin-right: 31px; }
  .main-nav a.is-active { color: var(--brand-blue-text); }
  .btn { position: absolute; display: flex; align-items: center; justify-content: center; color: var(--white); font-weight: 800; font-size: 9.5px; letter-spacing: .3px; text-decoration: none; box-shadow: 1px 2px 2px rgba(0,0,0,.25); }
  .btn-orange { background: var(--orange); }
  .btn-blue { background: var(--brand-blue); }

  /* hero */
  .hero { position: absolute; left: 0; top: 60px; width: 800px; height: 250px; }
  .hero-photo { position: absolute; inset: 0; background: linear-gradient(180deg, var(--hero-top), var(--hero-bottom)); }
  .hero-quote { position: absolute; left: 0; width: 800px; top: 86px; text-align: center; font-family: "Indie Flower", cursive; font-weight: 400; font-size: 36px; color: var(--white); }

  .script-title { position: absolute; left: 0; width: 800px; text-align: center; font-family: "Indie Flower", cursive; font-weight: 400; font-size: 25px; color: var(--ink); }

  /* services */
  .services { position: absolute; left: 0; top: 310px; width: 800px; height: 300px; background: var(--sky); }
  .service { position: absolute; top: 70px; width: 180px; text-align: center; }
  .service-icon { width: 52px; height: 52px; border-radius: 50%; background: var(--icon-fill); margin: 0 auto; box-shadow: 1px 2px 2px rgba(0,0,0,.15); }
  .service-title { margin-top: 13px; font-weight: 800; font-size: 9.5px; letter-spacing: .4px; color: var(--ink); }
  .service-text { margin: 10px auto 0; width: 132px; font-size: 7.8px; line-height: 12px; color: var(--ink-soft); }

  /* about */
  .about-photo { position: absolute; left: 100px; top: 679px; width: 290px; height: 172px; background: linear-gradient(135deg, var(--photo-a), var(--photo-b)); }
  .about-text { position: absolute; left: 412px; top: 677px; width: 292px; font-size: 8px; line-height: 12px; color: var(--ink-soft); }
  .about-text p + p { margin-top: 7px; }

  /* questions */
  .questions { position: absolute; left: 0; top: 876px; width: 800px; height: 275px; background: var(--sky); }
  .questions-deco { position: absolute; left: 142px; top: 72px; width: 126px; height: 124px; background: var(--sky-deco); opacity: .5; }
  .q-intro { position: absolute; left: 0; width: 800px; text-align: center; font-size: 8.8px; color: var(--ink-soft); }
  .q-dots { position: absolute; left: 0; width: 800px; text-align: center; font-size: 8px; line-height: 4px; letter-spacing: 1px; color: var(--orange); font-weight: 800; }
  .q-headline { position: absolute; left: 0; width: 800px; top: 171px; text-align: center; font-size: 15.5px; letter-spacing: .4px; color: var(--brand-blue-text); }
  .q-small { font-size: 6.5px; }

  /* footer */
  .site-footer { position: absolute; left: 0; top: 1151px; width: 800px; height: 49px; background: var(--brand-blue); color: var(--white); }
  .copyright { position: absolute; left: 100px; top: 20px; font-size: 7px; font-weight: 600; }
  .footer-brand { position: absolute; left: 0; width: 800px; top: 17px; text-align: center; font-weight: 800; font-size: 11px; letter-spacing: 1px; }
  .footer-nav { position: absolute; right: 100px; top: 20px; display: flex; gap: 8px; font-size: 7.5px; font-weight: 600; }
  .footer-nav a { color: var(--white); text-decoration: none; }
</style>
</head>
<body>

<header class="site-header">
  <div class="brand"><span class="brand-mark"></span><span class="brand-name">BRIGHT KELP</span></div>
  <nav class="main-nav">
    <a class="is-active" href="#">HOME</a>
    <a href="#">SERVICES</a>
    <a href="#">BLOG</a>
    <a href="#">ABOUT ME</a>
  </nav>
  <a class="btn btn-orange" href="#" style="left:615px;top:34px;width:85px;height:21px;">CONTACT ME</a>
</header>

<section class="hero">
  <div class="hero-photo" role="img" aria-label="Photo of a person seen from behind facing a wall of sketches and notes"></div>
  <h1 class="hero-quote">"...because ideas are a million"</h1>
</section>

<section class="services">
  <h2 class="script-title" style="top:19px;">How can I help you with your idea?</h2>

  <div class="service" style="left:72px;">
    <div class="service-icon" role="img" aria-label="Illustration of a teaching session"></div>
    <h3 class="service-title">I WILL TEACH YOU</h3>
    <p class="service-text">I want to learn at my own pace. You teach me how things are done and how it works and I will do it myself.</p>
  </div>
  <a class="btn btn-orange" href="#" style="left:120px;top:214px;width:86px;height:21px;">TEACH ME</a>

  <div class="service" style="left:308px;">
    <div class="service-icon" role="img" aria-label="Illustration of two people working together"></div>
    <h3 class="service-title">WE DO IT TOGETHER</h3>
    <p class="service-text">I want to learn how it worksand want to do it but I need someone that works along side with me.</p>
  </div>
  <a class="btn btn-orange" href="#" style="left:357px;top:214px;width:86px;height:21px;">LET’S DO IT</a>

  <div class="service" style="left:546px;">
    <div class="service-icon" role="img" aria-label="Illustration of a person handling the work"></div>
    <h3 class="service-title">I’LL DO IT FOR YOU</h3>
    <p class="service-text">I have this great idea butI just want to have it done for me. I don’t wont to do it or even learn about it.</p>
  </div>
  <a class="btn btn-orange" href="#" style="left:593px;top:214px;width:86px;height:21px;">DO IT FOR ME</a>
</section>

<section class="about">
  <h2 class="script-title" style="top:623px;">why should you hire my services?</h2>
  <div class="about-photo" role="img" aria-label="Portrait photo of the consultant outdoors on a residential street"></div>
  <div class="about-text">
    <p>Lorem ipsum dolor sit amet, consectetur adipisicing elit, sed do eiusmod tempor incididunt ut labore et dolore magna aliqua. Ut enim ad minim veniam, quis nostrud exercitation ullamco laboris nisi ut aliquip ex ea commodo consequat. Duis aute irure dolor in reprehenderit in voluptate velit esse cillum dolore eu fugiat nulla pariatur. Excepteur sint occaecat cupidatat non proident, sunt in culpa qui officia deserunt mollit anim id est laborum. Sed ut perspiciatis unde omnis iste natus error sit voluptatem accusantium doloremque laudantium, totam rem aperiam, eaque ipsa quae ab illo inventore veritatis et quasi architecto beatae vitae dicta sunt explicabo.</p>
    <p>Neque porro quisquam est, qui dolorem ipsum.</p>
  </div>
  <a class="btn btn-blue" href="#" style="left:412px;top:831px;width:85px;height:20px;">READ MORE</a>
</section>

<section class="questions">
  <div class="questions-deco" role="img" aria-label="Faint decorative illustration of a question in a speech bubble"></div>
  <h2 class="script-title" style="top:18px;">Do you have any questions?</h2>
  <p class="q-intro" style="top:58px;">It’s ok if you have questions.We haven’t worked together or meath each other so how do you now if:</p>
  <p class="q-intro" style="top:75px;">We can work together?</p>
  <div class="q-dots" style="top:91px;">•••</div>
  <p class="q-intro" style="top:98px;">Understand each other?</p>
  <div class="q-dots" style="top:112px;">•••</div>
  <p class="q-intro" style="top:119px;">(Did I say work together?)</p>
  <div class="q-dots" style="top:135px;">•••</div>
  <p class="q-intro" style="top:142px;">I have the experience you are looking for?</p>
  <p class="q-headline">Don’t worry about anything.</p>
  <p class="q-intro" style="top:191px;">I’m here for you!</p>
  <p class="q-intro" style="top:205px;">Use the button bellow to book a time slot where we can have a chat about what you need help with and we will take it from there.</p>
  <p class="q-intro q-small" style="top:221px;">With coffee included ofcourse!</p>
  <a class="btn btn-orange" href="#" style="left:358px;top:233px;width:85px;height:21px;">BOOK ME!</a>
</section>

<footer class="site-footer">
  <p class="copyright">Copyright @ 2018 BrightKelp. All rights reserved.</p>
  <div class="footer-brand">BRIGHT KELP</div>
  <nav class="footer-nav">
    <a href="#">Home</a><a href="#">Services</a><a href="#">Blog</a><a href="#">About me</a><a href="#">Contact me</a>
  </nav>
</footer>

</body>
</html>
```